Task Description:
I’m wanting a professionally designed 8 ½' x 11, 3 fold brochure, both sides, to print as my target audience are those people who primarily don’t have access to the internet. These items will be dropped off in the mailboxes of all households in the city.
However I do have a web site www.brightcivicpath.ca where I would like to have it as a document that can be down loaded.
This is my first foray into political office and my message needs to be clear, concise and easy to understand. The brochure should be a bit conservative yet be warm and inviting. I’ve selected two pictures that I think make sense under their respective headings, but I'm open to suggestions.I need to update my picture for the front cover.
There is the possibility of having T shirts and business cards made up, which would be in essence a simpler version of the brochure so please keep this in mind. I ask that you work with me and I will compensate you accordingly for the extras should they be required. You may want to consider making the Bright Civic Path into a logo as we own all the web extensions and have applied for copyright protection for branding purposes.
You may want to look at QM Larchfield http://www.qmlarchfield.ca/ , or the Pinecrest Bank of Canada www.pinecrestbank.com as two recognizable colour schemes here in Canada but don’t let that limit your imagination.
The content in the flier should remain intact although I am open to some minor suggestions. As you can see my talents as a graphic artist are limited hence my need for that professional make over that will give it a bit of razzle dazzle and set me out from the other candidates. So use your imagination!!
Target Market(s)
Middle age voters who may or may not have access to the internet and still prefer print
Industry/Entity Type
Conservative

```html
<!DOCTYPE html>
<html lang="en">
<head>
<meta charset="utf-8">
<title>Dale Marsh – Bright Civic Path brochure</title>
<link rel="stylesheet" href="https://fonts.googleapis.com/css2?family=Archivo+Black&family=Libre+Baskerville:ital,wght@0,400;0,700;1,400;1,700&display=swap">
<style>
  :root{
    --green-deep:#1c5e26;
    --green:#2f8a34;
    --green-mid:#4da23c;
    --green-light:#8cc63f;
    --green-pale:#e4f1d6;
    --ink:#2a2a2a;
    --paper:#ffffff;
    --rule:#bdbdbd;
  }
  *{box-sizing:border-box;margin:0;padding:0}
  html,body{width:773px;height:1200px;overflow:hidden;background:var(--paper)}
  body{position:relative;font-family:"Libre Baskerville",Georgia,serif;color:var(--ink)}
  .sheet{position:absolute;left:0;width:773px;overflow:hidden;background:var(--paper)}
  .sheet-outside{top:0;height:582px;border-bottom:1px solid var(--rule)}
  .sheet-inside{top:602px;height:598px;border-top:1px solid var(--rule)}
  .sheet-art{position:absolute;inset:0}
  .panel{position:absolute;top:0;height:100%;width:257px}
  .body-copy{font-size:7.6px;line-height:1.45}
  .body-copy p{margin-bottom:7px}
  .tag-box{position:absolute;background:var(--paper);border:2px solid var(--green);border-radius:14px;
    color:var(--green);font-style:italic;font-weight:700;text-align:center;box-shadow:0 2px 4px rgba(0,0,0,.25)}
  .site-url{position:absolute;font-size:9px;color:var(--green-deep);letter-spacing:.3px}
  /* outside */
  .bio .tag-box{left:40px;top:14px;width:150px;padding:6px 4px;font-size:14px;line-height:1.15}
  .bio .tag-box small{display:block;font-size:10px}
  .bio .body-copy{position:absolute;left:16px;top:96px;width:226px}
  .bio ul{padding-left:12px;margin-bottom:7px}
  .bio li{margin-bottom:3px}
  .vision .body-copy{position:absolute;left:18px;top:16px;width:222px}
  .vote-call{position:absolute;left:0;width:257px;top:392px;text-align:center;color:var(--green)}
  .vote-call .date{font-size:16px;font-weight:700;line-height:1.3}
  .vote-call .name{font-family:"Archivo Black",sans-serif;font-size:26px;color:var(--green-deep);margin-top:2px}
  .vision .site-url{left:0;width:257px;text-align:center;top:540px;color:var(--paper)}
  .cover .tag-box{left:62px;top:16px;width:180px;padding:8px 6px;font-size:13px;line-height:1.3}
  .cover-name{position:absolute;left:10px;top:204px;width:104px;font-family:"Archivo Black",sans-serif;color:var(--ink);font-size:21px;line-height:1.1}
  .cover-photo{position:absolute;left:122px;top:176px;width:122px;height:150px;border:3px solid var(--paper);
    background:linear-gradient(160deg,#d9d2c6,#8b8f8a 60%,#4f5753);box-shadow:0 1px 4px rgba(0,0,0,.35)}
  .cover-title{position:absolute;left:18px;top:380px;font-family:"Archivo Black",sans-serif;color:var(--green);font-size:27px;line-height:1.05}
  /* inside */
  .masthead-title{position:absolute;left:16px;top:22px;font-style:italic;font-weight:700;font-size:17px;color:var(--paper);white-space:nowrap}
  .masthead-title .badge{display:inline-block;width:26px;height:26px;border-radius:50%;background:var(--green-pale);vertical-align:middle;margin-right:8px}
  .city-strip{position:absolute;left:262px;top:14px;width:500px;height:66px;
    background:linear-gradient(180deg,#9fc3d8 0%,#c9d7c0 50%,#6b7f5a 100%);border:2px solid var(--paper)}
  .column .tag-box{top:110px;left:32px;width:194px;padding:7px 4px;font-size:13px;line-height:1.2}
  .column .body-copy{position:absolute;left:16px;top:162px;width:226px}
  .column.safety .body-copy{top:152px}
  .safety .tag-box{top:104px}
  .community-photo{position:absolute;left:18px;top:418px;width:222px;height:110px;border:2px solid var(--paper);
    background:linear-gradient(170deg,#b7c9b0,#6d8a5c 55%,#3e5233);box-shadow:0 1px 4px rgba(0,0,0,.3)}
  .photo-caption{position:absolute;left:18px;top:530px;width:222px;font-size:6.5px;font-style:italic;text-align:center}
  .sheet-inside .site-url{left:515px;width:257px;text-align:center;top:576px;color:var(--paper)}
</style>
</head>
<body>

<section class="sheet sheet-outside">
  <svg class="sheet-art" width="773" height="582" viewBox="0 0 773 582" aria-hidden="true">
    <defs>
      <linearGradient id="g-wave" x1="0" y1="0" x2="1" y2="1">
        <stop offset="0" stop-color="#8cc63f"/><stop offset="1" stop-color="#1c5e26"/>
      </linearGradient>
    </defs>
    <path d="M0 0H257V30C190 60 90 70 0 110Z" fill="url(#g-wave)"/>
    <path d="M0 110C90 70 190 60 257 30V40C190 72 90 84 0 122Z" fill="#8cc63f"/>
    <path d="M0 548C80 520 170 520 257 540V582H0Z" fill="url(#g-wave)"/>
    <path d="M0 540C80 510 170 510 257 530V536C170 518 80 520 0 548Z" fill="#8cc63f"/>
    <path d="M257 520C340 500 430 505 515 525V582H257Z" fill="url(#g-wave)"/>
    <line x1="257" y1="0" x2="257" y2="582" stroke="#e2e2e2"/>
    <line x1="515" y1="0" x2="515" y2="582" stroke="#e2e2e2"/>
    <path d="M515 0H773V150C700 110 600 110 515 160Z" fill="url(#g-wave)"/>
    <path d="M515 160C600 110 700 110 773 150V162C700 124 600 126 515 172Z" fill="#8cc63f"/>
    <path d="M515 350C620 330 700 340 773 370V480C690 440 600 440 515 470Z" fill="url(#g-wave)" opacity=".9"/>
    <path d="M515 470C600 440 690 440 773 480V494C690 456 600 456 515 484Z" fill="#8cc63f"/>
    <path d="M515 500C600 470 690 470 773 510V582H515Z" fill="#eef6e4"/>
  </svg>

  <div class="panel bio" style="left:0">
    <div class="tag-box"><small>Getting to know</small>Bright Civic Path</div>
    <div class="body-copy">
      <p><b>Dale Marsh</b> is a life long resident of Harbour Falls.</p>
      <p>My family has served this community and area for more than 100 years.</p>
      <ul>
        <li>Sales Manager for a regional supply firm for twenty years</li>
        <li>Past President of the Harbour Falls Business Association</li>
        <li>Active volunteer with local youth sport and service clubs</li>
        <li>Board member of the Community Arts Council</li>
      </ul>
      <p>Although I have a business career, I have always made time for the people who live here and the issues that matter to them.</p>
      <p>As manager I work with more than forty staff members every day. I know how to listen, build a team and keep a budget balanced.</p>
    </div>
  </div>

  <div class="panel vision" style="left:257px">
    <div class="body-copy">
      <p>I'm currently involved with Voltrex Labs Inc. a newly created R&amp;D company developing clean power systems for the transit industry. Our research partners consist of faculty and students from Northshore University. I have been able to see first hand what it takes to start, finance and run a new business in this city.</p>
      <p>As your mayor, my goal is to serve for two terms. With the support of council and residents we will build a plan that sees our city grow, attract new employers and keep our young people here at home.</p>
      <p>I believe we need a council that works together, spends wisely and puts residents first. I look forward to meeting you on your doorstep.</p>
    </div>
    <div class="vote-call">
      <div class="date">On October 25th<br>Vote</div>
      <div class="name">Dale Marsh</div>
    </div>
    <div class="site-url">www.brightcivicpath.ca</div>
  </div>

  <div class="panel cover" style="left:515px">
    <div class="tag-box">Unlock the Potential of the Best Small City in North America</div>
    <div class="cover-name">DALE<br>MARSH</div>
    <div class="cover-photo" role="img" aria-label="Portrait photograph of the candidate"></div>
    <div class="cover-title">BRIGHT<br>CIVIC<br>PATH</div>
  </div>
  <div class="site-url" style="left:515px;width:257px;text-align:center;top:552px">www.brightcivicpath.ca</div>
</section>

<section class="sheet sheet-inside">
  <svg class="sheet-art" width="773" height="598" viewBox="0 0 773 598" aria-hidden="true">
    <defs>
      <linearGradient id="g-head" x1="0" y1="0" x2="0" y2="1">
        <stop offset="0" stop-color="#2f8a34"/><stop offset="1" stop-color="#1c5e26"/>
      </linearGradient>
      <linearGradient id="g-foot" x1="0" y1="0" x2="1" y2="0">
        <stop offset="0" stop-color="#8cc63f"/><stop offset="1" stop-color="#1c5e26"/>
      </linearGradient>
    </defs>
    <rect x="0" y="0" width="773" height="94" fill="url(#g-head)"/>
    <path d="M0 94C250 80 520 80 773 94V100H0Z" fill="#8cc63f"/>
    <line x1="257" y1="100" x2="257" y2="550" stroke="#e2e2e2"/>
    <line x1="515" y1="100" x2="515" y2="550" stroke="#e2e2e2"/>
    <path d="M0 560C250 540 520 540 773 556V598H0Z" fill="url(#g-foot)"/>
    <path d="M0 552C250 532 520 532 773 548V556C520 540 250 540 0 560Z" fill="#8cc63f"/>
  </svg>

  <div class="masthead-title"><span class="badge"></span>Bright Civic Path</div>
  <div class="city-strip" role="img" aria-label="Panoramic photographs of the city waterfront and downtown"></div>

  <div class="panel column economy" style="left:0">
    <div class="tag-box">A Strong Economy</div>
    <div class="body-copy">
      <p>Without a strong economy we can't afford to pay for social services that we too often take for granted.</p>
      <p>Although the City is the largest corporation, it is unique in the fact that its revenue stream is tied directly to residents.</p>
      <p>Without new business and new citizens the burden of taxes will fall increasingly on residential taxpayers.</p>
      <p>Our demographics have changed over the years and those changes need to be reflected in the way we run the city.</p>
      <p>Our level of debt and our future commitments need to be effectively communicated to the people that own this city. You the tax payer.</p>
      <p>Currently our debt is a large sum and further commitments are planned. How will we pay for this?</p>
    </div>
  </div>

  <div class="panel column growth" style="left:257px">
    <div class="tag-box">New Opportunities<br>New Beginnings</div>
    <div class="body-copy">
      <p>As a city we need to celebrate the progress made on the most modern small city in North America and share it widely.</p>
      <p>That means, if you currently own and operate a business large or small we need your input to improve the efficiency of how we deliver services.</p>
      <p>If you're in the planning stages and need assistance, the city will be there to offer support and guidance.</p>
      <p>Regional projects are vitally important to the flow of goods and services.</p>
      <p>As your mayor I will aggressively promote this city to investors, partners and newcomers who share our vision for growth, potential and opportunities for young and old alike.</p>
      <p>Are we open for business... Absolutely!!</p>
    </div>
  </div>

  <div class="panel column safety" style="left:515px">
    <div class="tag-box">A Safe Community</div>
    <div class="body-copy">
      <p>Without a safe community it will be difficult to attract new people and new businesses to our community.</p>
      <p>I have a plan that will utilize the resources of the current police force to better facilitate the services that are currently provided.</p>
      <p>Incentive programs need to be initiated in all city departments at the ground level so that good ideas don't get lost in bureaucracy.</p>
      <p>Seniors and youth are the most vulnerable of all. I have a plan that will identify these groups and make sure they are heard.</p>
    </div>
    <div class="community-photo" role="img" aria-label="Photograph of a neighbourhood street scene"></div>
    <div class="photo-caption">Working together for a safer city</div>
  </div>

  <div class="site-url">www.brightcivicpath.ca</div>
</section>

</body>
</html>
```